Attractive & informative Sports Arena/Venue website project

Hi there

We are a Futsal (indoor football/soccer) venue business. We would like to create an informative website of our futsal venue.
Theme : Clear informative website, simplistic design, minimalistic design, easy to navigate, uncluttered.

Colour theme : Colourful theme - use Samba/Brazil as a reference.

Built on Wordpress.
Easy to edit and add pictures, fonts, add wordings, links to other websites.

What we require :

Tab information :
Home, Book Now, Our Venue & Courts, Futsal Academy, Futsal Online Store, Contact Us.

Homepage tab :

Static background, blurred and with opacity.
Reference : http://www.rovadeskwork.my/
Background follows the page even as you scroll down.
Reference : http://norahpelt.com/

Background must have this information on it clearly :

Play futsal, block book, host tournaments, corporate events,
birthday parties, eat & lepak, big screen projector, shop futsal gear, and more.

Book Now : +603-71046392
+603-71046318
+601198562207 (SMS/Chatline)
Email us : info@kilatarenacourts.com
Location : Kilat Arena Courts PJ, Lot 27 Seksyen 38C,
Jalan 419, Petaling Jaya 46100,
Selangor

Must have 3 buttons below the frontpage area
Reference : http://www.kilatgearhub.com.my/

Book Now button, Our Courts button, Malaysia's Futsal Academy - with RBL level coaches button.
All designed by web designer (simple design is sufficient)

Must have :
Chatterbook 'Like' page plugin
Snapgram feed plugin

Footer :
Follow the tabs , and add Chatterbook & Snapgram page buttons.

Homepage meta title :
Kilat Arena Courts venue - Petaling Jaya, Selangor

Homepage meta description :
Top class futsal venue located in PJ for rubber courts & grass courts. Bookings : +603-71046392.
Located on Jalan 419, PJ, next to Orchid Expressway. Landmarks : PJ Grandlay, Tero Plaza, Cendana Hotel, Menara Orbis, Velmont Mall.

Book Now tab :
Must have a space to put our contact information clearly.

Below this we have an Online Booking wording, and a picture/button that says Book Online Now which opens a new tab & leads to a seperate website for online booking.

Our Venue & Courts tab :
We need to be able to add information in here in this format :
Reference : http://www.quillory.com/
Able to add pictures, wordings, information, link to other websites, etc.

Futsal Academy tab :

Futsal Online Store :

Contact Us :

Please be able to forward to our domain : www.kilatarenacourts.com, and forward to our domain host server.

We would like to use this website theme for you to reuse & create other websites for us using the same theme. Please contact us after this site is done. ray@vonmerik.com

Thank you!
Updates

Project Deadline Extended
Reason: Mistakenly set it at 5 days. We prefer 10 days to give designers a chance to work on this without too much time constraints & allow them more creative freedom to design this

Target Market(s)

Sports Enthusiast, Futsal & Football enthusiast,

Industry/Entity Type

Shop

Number of Pages Required

5+ page

Font styles to use
Sans Serif

Requirements
Must have
• Must have :
• Chatterbook 'Like' page plugin
• Snapgram feed plugin
• We would like to use this website theme for you to reuse & create other websites for us using the same theme. Please contact us after this site is done. ray@vonmerik.com
Nice to have
• Theme : Clear informative website, simplistic design, minimalistic design, easy to navigate, uncluttered.

```html
<!DOCTYPE html>
<html lang="en">
<head>
<meta charset="utf-8">
<title>Kilat Arena Courts venue - Petaling Jaya, Selangor</title>
<link href="https://fonts.googleapis.com/css2?family=Raleway:wght@400;500&family=Open+Sans:wght@400;600&display=swap" rel="stylesheet">
<style>
:root{
  --blue:#1a73c4;--blue-dark:#0f5ea8;--blue-light:#2d8ad8;
  --orange:#e68a1e;--ink:#333;--muted:#888;--head:#1f5d9c;
  --line:#d6d6d6;--foot:#f3f3f3;--green:#2f9a3a;
}
*{box-sizing:border-box;margin:0;padding:0}
html,body{width:918px;height:1200px;overflow:hidden;background:#fff}
body{font-family:"Open Sans",sans-serif;color:var(--ink);position:relative}
.brand{position:absolute;left:107px;top:28px;display:flex;align-items:center;gap:10px}
.brand-mark{width:26px;height:26px;background:var(--green)}
.brand-name{font-family:"Raleway",sans-serif;font-weight:500;font-size:22px;color:var(--green)}
.main-nav{position:absolute;top:90px;left:0;width:918px;height:37px;background:linear-gradient(var(--blue-light),var(--blue-dark));display:flex;justify-content:center}
.main-nav a{font-family:"Raleway",sans-serif;font-size:11.5px;color:#fff;text-decoration:none;line-height:37px;padding:0 14px;border-left:1px solid rgba(255,255,255,.25)}
.main-nav a:first-child{border-left:none}
.hero{position:absolute;top:127px;left:0;width:918px;height:399px;background:radial-gradient(ellipse at 30% 70%,#3d6b34 0%,#1c2a1c 35%,#111 70%)}
.hero-text{position:absolute;top:120px;left:0;width:918px;text-align:center;color:#fff;font-family:"Raleway",sans-serif}
.hero-text h1{font-weight:400;font-size:27px;margin-bottom:6px}
.hero-text p{font-size:21px;line-height:30px}
.dots{position:absolute;top:374px;left:430px;display:flex;gap:4px}
.dots span{width:12px;height:12px;border-radius:50%;background:#fff}
.dots span:first-child{background:var(--orange)}
.tile{position:absolute;top:545px;width:229px;height:143px;box-shadow:0 10px 10px -6px rgba(0,0,0,.3)}
.tile-photo{height:105px}
.tile-bar{height:38px;display:flex;align-items:center;justify-content:space-between;padding:0 16px;color:#fff;font-family:"Raleway",sans-serif}
.tile svg{width:10px;height:18px}
.feed{position:absolute;top:739px;width:345px;height:185px;border:1px solid var(--line)}
.feed h2{font-family:"Raleway",sans-serif;font-weight:400;font-size:14px;color:var(--head);height:34px;line-height:36px;padding-left:20px;background:linear-gradient(#fff,#ededed);border-bottom:1px solid var(--line)}
.post{display:flex;gap:14px;padding:15px 20px 0}
.thumb{width:35px;height:32px;flex:none;margin-top:2px}
.post h3{font-weight:400;font-size:9px;margin-bottom:3px}
.post p{font-size:6.8px;color:var(--muted);line-height:12px}
.site-footer{position:absolute;top:966px;left:0;width:918px;height:186px;background:linear-gradient(#fff,var(--foot));border-top:1px solid #e2e2e2}
.col{position:absolute;top:40px;font-size:9px;line-height:16px}
.col h4{font-family:"Raleway",sans-serif;font-weight:400;font-size:12.5px;margin-bottom:10px}
.col.sep{border-right:1px solid #ddd;height:104px}
.social a{color:var(--head);text-decoration:none;margin-right:8px}
.copy{position:absolute;top:1152px;left:0;width:918px;height:48px;border-top:1px solid #ddd;background:var(--foot);font-size:8px;padding:17px 131px}
</style>
</head>
<body>
<header>
  <div class="brand"><span class="brand-mark"></span><span class="brand-name">Kilat Arena Courts</span></div>
  <nav class="main-nav">
    <a href="#">HOME</a><a href="#">BOOK NOW</a><a href="#">OUR VENUE &amp; COURTS</a><a href="#">FUTSAL ACADEMY</a><a href="#">FUTSAL ONLINE STORE</a><a href="#">CONTACT US</a>
  </nav>
</header>
<section class="hero" role="img" aria-label="Futsal player heading a ball in a green shirt">
  <div class="hero-text">
    <h1>Play futsal, block book, host tournaments,</h1>
    <p>corporate events,birthday parties, eat &amp; lepak, big screen<br>projector, shop futsal gear, and more</p>
  </div>
  <div class="dots"><span></span><span></span><span></span><span></span></div>
</section>
<a class="tile" style="left:106px">
  <div class="tile-photo" role="img" aria-label="Player kicking a ball in a floodlit stadium" style="background:linear-gradient(#1d3d6a,#0d1a30)"></div>
  <div class="tile-bar" style="background:var(--orange);font-size:17px">Book Now<svg viewBox="0 0 10 18"><path d="M1 1l8 8-8 8" fill="none" stroke="#fff" stroke-width="1.3"/></svg></div>
</a>
<a class="tile" style="left:345px">
  <div class="tile-photo" role="img" aria-label="Players challenging for the ball near a goal" style="background:linear-gradient(#556,#2f5a2a)"></div>
  <div class="tile-bar" style="background:#1d1f1d;font-size:17px">Our Courts<svg viewBox="0 0 10 18"><path d="M1 1l8 8-8 8" fill="none" stroke="#fff" stroke-width="1.3"/></svg></div>
</a>
<a class="tile" style="left:583px">
  <div class="tile-photo" role="img" aria-label="Goalkeeper saving a shot in front of the net" style="background:linear-gradient(#ddd,#8a6f6f 70%,#4a8a3a)"></div>
  <div class="tile-bar" style="background:var(--blue);font-size:14px">Malaysia's Futsal Academy<svg viewBox="0 0 10 18"><path d="M1 1l8 8-8 8" fill="none" stroke="#fff" stroke-width="1.3"/></svg></div>
</a>
<section class="feed" style="left:106px">
  <h2>Chatterbook Feed</h2>
  <div class="post"><div class="thumb" role="img" aria-label="Post photo" style="background:#7a6a5a"></div><div><h3>Praesent elementum elit</h3><p>at tellus nec ultricies sit amet porttitor mattis enim In massa libero interdum<br>nec interdum vel blandit sed nulla In ullamcorper est eget tempor cursus</p><p>Praesent elementum elit at tellus nec ultricies sit<br>Posted 10 min ago</p></div></div>
  <div class="post"><div class="thumb" role="img" aria-label="Post photo" style="background:#8a8a8a"></div><div><h3>Cum sociis natoque penatibus</h3><p>at tellus nec ultricies sit amet porttitor mattis enim In massa libero interdum<br>nec interdum vel blandit sed nulla In ullamcorper est</p></div></div>
</section>
<section class="feed" style="left:465px;top:737px">
  <h2>Snapgram Feed</h2>
  <div class="post"><div class="thumb" role="img" aria-label="Post photo" style="background:#c05a4a"></div><div><h3>Praesent elementum elit</h3><p>at tellus nec ultricies sit amet porttitor mattis enim In massa libero interdum<br>nec interdum vel blandit sed nulla In ullamcorper est eget tempor cursus</p><p>Praesent elementum elit at tellus nec ultricies sit<br>Posted 10 min ago</p></div></div>
  <div class="post"><div class="thumb" role="img" aria-label="Post photo" style="background:#6a7a4a"></div><div><h3>Cum sociis natoque penatibus</h3><p>at tellus nec ultricies sit amet porttitor mattis enim In massa libero interdum<br>nec interdum vel blandit sed nulla In ullamcorper est</p></div></div>
</section>
<footer class="site-footer">
  <div class="col sep" style="left:131px;width:129px"><h4>INFORMATION</h4>Book Now<br>Our Venue &amp; Courts<br>Futsal Academy<br>Futsal Online Store<br>Contact Us</div>
  <div class="col sep" style="left:294px;width:182px"><h4>BOOK NOW</h4>Book Now : +603-71046392<br>+603-71046318<br>+601198562207 (SMS/Chatline)<br>Email us : info@kilatarenacourts.com</div>
  <div class="col sep" style="left:505px;width:159px"><h4>OUR ADDRESS</h4>Location : Kilat Arena Courts PJ, Lot<br>27 Seksyen 38C,<br>Jalan 419, Petaling Jaya 46100,<br>Selangor</div>
  <div class="col social" style="left:695px"><h4>GET IN TOUCH</h4><a href="#">Chatterbook</a><a href="#">Snapgram</a></div>
</footer>
<div class="copy">© 2015 Company Name&nbsp; All right reserved&nbsp; Term of Use</div>
</body>
</html>
```